Brindlewood Court Apartments Business Cards

We need a business card design for a small apartment community in the metro-Detroit area. The property has a park-like feel and is surrounded by trees and ponds.

The logo colors are:
R=9 G=117 B=127
R=210 G=183 B=114

Contact Information for Business Card

Marla Finch
Property Manager
Brindlewood Court Apartments
352 Brindlewood Way
Fernhollow, OH 48190
Phone (555)517-2039

```html
<!DOCTYPE html>
<html lang="en">
<head>
<meta charset="utf-8">
<title>Brindlewood Court Apartments – Business Cards</title>
<link rel="stylesheet" href="https://fonts.googleapis.com/css2?family=Arimo:wght@400;700&display=swap">
<style>
  :root {
    --canvas: #e9e6e1;
    --card-black: #0b0b0b;
    --card-sheen: #1d1d1d;
    --band-grey: #2e2e2f;
    --teal: #09757f;
    --teal-bright: #1aa3ad;
    --tan: #d2b772;
    --tan-pale: #cdbf97;
    --text-light: #e8e4da;
  }
  * { box-sizing: border-box; margin: 0; padding: 0; }
  html, body {
    width: 1200px; height: 1023px; overflow: hidden;
    background: var(--canvas);
    font-family: "Arimo", Arial, sans-serif;
  }
  .sheet {
    width: 1200px; height: 1023px;
    display: flex; flex-direction: column; align-items: center; justify-content: center;
    gap: 60px;
  }
  .card {
    position: relative;
    width: 700px; height: 400px;
    background: linear-gradient(160deg, var(--card-sheen) 0%, var(--card-black) 45%, var(--card-black) 100%);
    border-radius: 6px;
    overflow: hidden;
    box-shadow: 0 14px 30px rgba(0,0,0,.25);
  }
  .brand {
    position: absolute;
    display: flex; align-items: center; gap: 16px;
  }
  .brand-dot {
    flex: none;
    width: 44px; height: 44px; border-radius: 50%;
    background: var(--teal-bright);
  }
  .brand-name {
    font-weight: 700; color: var(--tan);
    letter-spacing: 2px; text-transform: uppercase;
    line-height: 1.2; text-align: center;
  }
  .brand-name span { display: block; }
  .card-front .brand { top: 58px; left: 250px; }
  .card-front .brand-name { font-size: 22px; }
  .card-front .brand-name .brand-sub { font-size: 12px; letter-spacing: 5px; }
  .contact {
    position: absolute; left: 48px; top: 190px;
    color: var(--text-light);
  }
  .contact-name {
    font-weight: 700; font-size: 22px; color: var(--tan);
    text-transform: uppercase; letter-spacing: .5px;
  }
  .contact-title { font-size: 17px; margin-top: 6px; }
  .contact-phone {
    display: flex; align-items: center; gap: 10px;
    font-size: 16px; margin-top: 12px;
  }
  .contact-phone svg { width: 16px; height: 16px; }
  .address-band {
    position: absolute; left: 0; right: 0; bottom: 18px; height: 72px;
    background: var(--band-grey);
    padding: 13px 48px;
    font-size: 16px; line-height: 1.4;
  }
  .address-company { color: var(--tan-pale); }
  .address-street { color: var(--text-light); }
  .edge-tan {
    position: absolute; left: 0; right: 0; bottom: 8px; height: 10px;
    background: var(--tan-pale);
  }
  .edge-teal {
    position: absolute; left: 0; right: 0; bottom: 0; height: 8px;
    background: var(--teal-bright);
  }
  .card-back .brand { left: 0; right: 0; top: 0; bottom: 0; justify-content: center; gap: 22px; }
  .card-back .brand-dot { width: 64px; height: 64px; }
  .card-back .brand-name { font-size: 32px; }
  .card-back .brand-name .brand-sub { font-size: 17px; letter-spacing: 7px; }
</style>
</head>
<body>
<main class="sheet">
  <section class="card card-front" aria-label="Business card front">
    <div class="brand">
      <span class="brand-dot"></span>
      <p class="brand-name"><span>Brindlewood Court</span><span class="brand-sub">Apartments</span></p>
    </div>
    <div class="contact">
      <p class="contact-name">Marla Finch</p>
      <p class="contact-title">Property Manager</p>
      <p class="contact-phone">
        <svg viewBox="0 0 24 24" aria-hidden="true"><path fill="#e8e4da" d="M6.6 10.8a15.1 15.1 0 0 0 6.6 6.6l2.2-2.2a1 1 0 0 1 1-.25 11.4 11.4 0 0 0 3.6.57 1 1 0 0 1 1 1V20a1 1 0 0 1-1 1A17 17 0 0 1 3 4a1 1 0 0 1 1-1h3.5a1 1 0 0 1 1 1c0 1.25.2 2.45.57 3.57a1 1 0 0 1-.25 1z"/></svg>
        (555)517-2039
      </p>
    </div>
    <div class="address-band">
      <p class="address-company">Brindlewood Court Apartments</p>
      <p class="address-street">352 Brindlewood Way Fernhollow, OH 48190</p>
    </div>
    <div class="edge-tan"></div>
    <div class="edge-teal"></div>
  </section>

  <section class="card card-back" aria-label="Business card back">
    <div class="brand">
      <span class="brand-dot"></span>
      <p class="brand-name"><span>Brindlewood Court</span><span class="brand-sub">Apartments</span></p>
    </div>
  </section>
</main>
</body>
</html>
```